New website design and logo for FusoBrite.com to help ignite the website sales.

Hi designers,

Fusobrite is a new welding brand that is selling welding equipement.

Currently I have around 5 to 10 products. The issue is that the site itself does not do that much of sales. So I have to do something about the seo etc. but that is out of scope for the design.

What is in scope is to comeup with a new logo and website look and feel that is in line with the customers.

men, non professionals, garage, home improvements, perhaps sme ( small mediul entreprice business that want to start in the welding industry.

Products are midrange prices and quality. The look and feel must breath cool stuff, sexy ( women in working cloths carrying welding gloves, other protection gear and weldels)

The wedsite is build in wordpress with the Divi theme. I am an IT guy myself withhout any creativity in me :( so if you can help me with that that would be great.

Please have a quick look at fusobrite.com

Best regards,
Joost

Target Market(s)

non professional welders that do metal work in there garage

Coding

Coded - Design and coding required

Number of Pages Required

3 page

Font styles to use
Sans Serif

Colors
0355a3
ffc214

Requirements
Must have
• I would like to see a new homepage and product page design together with a new logo.
Nice to have
• shop design

```html
<!DOCTYPE html>
<html lang="en">
<head>
<meta charset="utf-8">
<title>FusoBrite.com – Welding Equipment</title>
<link rel="stylesheet" href="https://fonts.googleapis.com/css2?family=Figtree:wght@400;500;600;700;800&display=swap">
<style>
:root{
  --navy:#17487d;
  --navy-deep:#0d2f57;
  --red:#e8141b;
  --ink:#1d1d1d;
  --text:#333;
  --white:#fff;
}
*{box-sizing:border-box;margin:0;padding:0}
html,body{width:1200px;height:3899px;overflow:hidden;background:var(--white)}
body{font-family:"Figtree",sans-serif;color:var(--ink);position:relative}
.abs{position:absolute}

/* header */
.brand{left:172px;top:66px;display:flex;align-items:center;gap:10px;font-size:22px;font-weight:700;color:var(--navy)}
.brand-dot{width:22px;height:22px;border-radius:50%;background:var(--red);flex:none}
.nav{left:553px;top:53px;display:flex;gap:25px;font-size:14px;font-weight:600;color:#222}
.nav-btn{width:40px;height:40px;border-radius:50%;top:43px;display:flex;align-items:center;justify-content:center}
.nav-btn.cart{left:933px;background:var(--navy)}
.nav-btn.search{left:986px;background:var(--red)}

/* hero */
.hero{left:0;top:113px;width:1200px;height:694px;
  background:
    radial-gradient(ellipse 260px 200px at 66% 82%,rgba(190,230,245,.85) 0%,rgba(90,170,210,.45) 45%,rgba(0,0,0,0) 100%),
    radial-gradient(ellipse 330px 260px at 78% 32%,rgba(70,150,200,.75) 0%,rgba(30,90,130,.35) 55%,rgba(0,0,0,0) 100%),
    radial-gradient(ellipse 420px 300px at 88% 75%,rgba(200,110,40,.35) 0%,rgba(0,0,0,0) 100%),
    linear-gradient(90deg,#07090c 0%,#0d141c 45%,#15283a 100%)}
.hero-title{left:172px;top:222px;font-size:31px;line-height:41px;font-weight:800;color:var(--white)}
.hero-sub{left:172px;top:322px;font-size:21px;color:var(--white);font-weight:500}
.btn-outline{left:172px;top:393px;width:114px;height:54px;border:2px solid var(--white);color:var(--white);
  font-size:14px;font-weight:600;display:flex;align-items:center;justify-content:center}
.hero-arrows{left:172px;top:512px}

/* steps */
.steps{left:172px;top:662px;width:856px;height:253px;background:var(--navy);display:flex;padding:50px 28px 0 28px;
  box-shadow:0 22px 20px -14px rgba(0,0,0,.35)}
.step{flex:1;position:relative;padding-left:25px;color:var(--white)}
.step .num{position:absolute;left:0;top:-8px;font-size:58px;font-weight:700;color:rgba(255,255,255,.16);line-height:1}
.step h3{position:relative;font-size:19px;font-weight:700;margin-top:16px;white-space:nowrap}
.step .bar{width:96px;height:2px;background:rgba(255,255,255,.7);margin:24px 0 18px -25px}
.step p{font-size:13px;line-height:22px;width:210px}

/* intro */
.intro-title{left:0;width:1200px;top:1003px;text-align:center;font-size:23px;line-height:31px;font-weight:800;color:var(--navy)}
.intro-text{left:172px;width:856px;top:1090px;text-align:center;font-size:12px;line-height:24px;color:var(--text)}
.intro-text p+p{margin-top:11px}
.prod-box{width:333px;height:348px;border:1px solid #555;top:1281px;padding:20px}
.prod-label{top:1655px;width:333px;text-align:center;font-size:18px;font-weight:700}
.ph{display:block;width:100%;height:100%}

/* products band */
.band{left:0;top:1780px;width:1200px;height:620px;
  background:radial-gradient(ellipse 500px 300px at 85% 10%,rgba(60,110,170,.5) 0%,rgba(0,0,0,0) 100%),
  linear-gradient(120deg,#1c5289 0%,#0f3766 55%,#0a2a52 100%)}
.band-title{left:0;width:1200px;top:1856px;text-align:center;font-size:27px;font-weight:800;color:var(--white)}
.card{top:1956px;width:248px;height:256px;background:var(--white);padding:18px}
.card-name{top:2237px;width:248px;text-align:center;font-size:20px;font-weight:700;color:var(--white)}
.card-price{top:2276px;width:248px;text-align:center;font-size:18px;font-weight:700;color:var(--white)}
.card-price s{font-weight:500;margin-right:6px}

/* featured */
.feat-title{left:0;width:1200px;top:2482px;text-align:center;font-size:27px;font-weight:800;color:var(--navy)}
.feat{top:2566px;width:418px;height:240px;border:1px solid #777;padding:8px;display:flex;gap:12px}
.feat .ph{width:224px;height:224px;flex:none}
.feat h4{font-size:12px;line-height:22px;font-weight:700;margin-top:12px;text-transform:uppercase}
.feat p{font-size:11px;line-height:19.5px;color:var(--text);margin-top:12px;text-align:justify}

/* quote */
.quote-photo{left:361px;top:2916px;width:839px;height:559px;
  background:radial-gradient(ellipse 120px 80px at 48% 78%,rgba(180,215,240,.8) 0%,rgba(0,0,0,0) 100%),
  radial-gradient(ellipse 260px 280px at 68% 55%,rgba(60,55,40,.85) 0%,rgba(0,0,0,0) 100%),
  linear-gradient(180deg,#c7ced5 0%,#96a2ad 40%,#6b6357 70%,#3d352b 100%)}
.quote-title{left:172px;top:3024px;font-size:27px;font-weight:800;color:var(--white)}
.field{background:var(--white);font-size:12px;color:#333;padding:17px 12px}
.submit{left:172px;top:3322px;width:105px;height:43px;background:var(--red);color:var(--white);font-size:14px;font-weight:700;display:flex;align-items:center;justify-content:center}

/* footer */
.foot-brand{left:172px;top:3680px;display:flex;align-items:center;gap:12px;font-size:26px;font-weight:700;color:var(--navy)}
.foot-brand .brand-dot{width:26px;height:26px}
.foot-col h5{font-size:14px;font-weight:600;margin-bottom:16px}
.foot-col li{list-style:none;font-size:12px;line-height:30px}
.about p{font-size:12px;line-height:22px;width:187px;text-align:justify}
.email{left:825px;top:3604px;width:203px;height:44px;border:1px solid #333;font-size:12px;padding:14px 9px}
.sub-btn{left:825px;top:3668px;width:89px;height:44px;background:var(--red);color:var(--white);font-size:13px;font-weight:600;display:flex;align-items:center;justify-content:center}
.rule{left:172px;top:3800px;width:856px;height:1px;background:#444}
.copy{left:172px;top:3835px;font-size:12px}
.social{left:872px;top:3830px;display:flex;gap:6px}
.social span{width:26px;height:26px;border-radius:50%;background:#111;display:block}
</style>
</head>
<body>

<!-- header -->
<div class="abs brand"><span class="brand-dot"></span>FusoBrite.com</div>
<nav class="abs nav"><span>Home</span><span>Products</span><span>Shopping Cart</span><span>My Account</span></nav>
<div class="abs nav-btn cart"><svg width="20" height="18" viewBox="0 0 20 18" fill="none" stroke="#fff" stroke-width="2"><path d="M1 2h3l2 9h10l2-7H5"/><circle cx="8" cy="15" r="1.5"/><circle cx="15" cy="15" r="1.5"/></svg></div>
<div class="abs nav-btn search"><svg width="18" height="18" viewBox="0 0 18 18" fill="none" stroke="#fff" stroke-width="2.4"><circle cx="7.5" cy="7.5" r="5"/><path d="M11 11l5 5"/></svg></div>

<!-- hero -->
<section class="abs hero" role="img" aria-label="Welder in a helmet working on steel with sparks flying"></section>
<h1 class="abs hero-title">SIMPLE WELDING OF STEEL<br>&amp; ALUMINUM</h1>
<div class="abs hero-sub">Get great results with tools that work</div>
<div class="abs btn-outline">SHOP NOW</div>
<svg class="abs hero-arrows" width="60" height="44" viewBox="0 0 60 44" fill="none" stroke="#fff" stroke-width="2.5"><path d="M18 4L3 22l15 18"/><path d="M40 4l15 18-15 18"/></svg>

<div class="abs steps">
  <div class="step"><span class="num">01</span><h3>GIVE US A CALL</h3><div class="bar"></div><p>Your official source for 24/7 fusobrite support.</p></div>
  <div class="step"><span class="num">02</span><h3>EVALUATE THE COST</h3><div class="bar"></div><p>Cost analysis helps evaluate contract profitability.</p></div>
  <div class="step"><span class="num">03</span><h3>GET THE JOB DONE!</h3><div class="bar"></div><p>To fulfil one's task, to do what is required to do.</p></div>
</div>

<!-- intro -->
<h2 class="abs intro-title">WAARMEE BESCHERMT U UW HANDEN TIJDENS<br>HET LASSEN?</h2>
<div class="abs intro-text">
  <p>Werkt u met oude versleten, hard geworden lashandschoenen, of last u met bouwhandschoenen (!) of nog erger last u met blote handen (!!), dan stelt u uw huid bloot aan gevaar. Pas op daarmee. Een lasdruppel van ruim 1200 graden brand gemakkelijk door een goedkope bouwhand schoen heen. Ook bij oud versleten handschoenen is een brandplek snel opgelopen.</p>
  <p>Bij het lassen komt veel uv-licht vrij. Met verkeerde of te korte handschoenen zijn uw handen of onderarmen al na een paar minuten verbrand. Onderschat een beetje rood verbrande huid niet, want op langere termijn kan dit slechte gevolgen hebben voor uw huid.</p>
</div>
<div class="abs prod-box" style="left:221px"><div class="ph" role="img" aria-label="Black leather welding gloves" style="background:radial-gradient(ellipse 30% 42% at 50% 50%,#3a3a34 0%,#6e6e66 55%,#fff 100%)"></div></div>
<div class="abs prod-box" style="left:626px"><div class="ph" role="img" aria-label="Blue and grey MIG welding machine" style="background:radial-gradient(ellipse 42% 34% at 50% 50%,#5d8ed6 0%,#a9bdd9 55%,#fff 100%)"></div></div>
<div class="abs prod-label" style="left:221px">WELDING GLOVES</div>
<div class="abs prod-label" style="left:626px">MIG-2500</div>

<!-- our products -->
<section class="abs band" role="img" aria-label="Dark blue toned welding workshop background"></section>
<h2 class="abs band-title">OUR PRODUCTS</h2>
<svg class="abs" style="left:70px;top:2080px" width="34" height="28" viewBox="0 0 34 28" fill="none" stroke="#fff" stroke-width="3.5"><path d="M32 14H4M15 3L4 14l11 11"/></svg>
<svg class="abs" style="left:1098px;top:2080px" width="34" height="28" viewBox="0 0 34 28" fill="none" stroke="#fff" stroke-width="3.5"><path d="M2 14h28M19 3l11 11-11 11"/></svg>
<div class="abs card" style="left:172px"><div class="ph" role="img" aria-label="Red and black MIG welder" style="background:radial-gradient(ellipse 34% 40% at 50% 50%,#c62b24 0%,#b3766f 55%,#fff 100%)"></div></div>
<div class="abs card" style="left:476px"><div class="ph" role="img" aria-label="Blue and grey MIG welding machine" style="background:radial-gradient(ellipse 42% 34% at 50% 50%,#5d8ed6 0%,#a9bdd9 55%,#fff 100%)"></div></div>
<div class="abs card" style="left:780px"><div class="ph" role="img" aria-label="Black auto-darkening welding helmet" style="background:radial-gradient(ellipse 30% 38% at 52% 50%,#2a2a2a 0%,#77717f 55%,#fff 100%)"></div></div>
<div class="abs card-name" style="left:172px">MIG-250P</div>
<div class="abs card-name" style="left:476px">MIG-2500</div>
<div class="abs card-name" style="left:780px">WELDING HELMET</div>
<div class="abs card-price" style="left:172px"><s>€845,00</s>€795,00</div>
<div class="abs card-price" style="left:476px">€745,00</div>
<div class="abs card-price" style="left:780px">€109,00</div>

<!-- featured -->
<h2 class="abs feat-title">FEATURED PRODUCTS</h2>
<div class="abs feat" style="left:172px">
  <div class="ph" role="img" aria-label="Black speed square measuring tool" style="background:linear-gradient(135deg,#d9d4cc 0%,#b3ada3 40%,#2a2a28 62%,#1a1a18 80%,#5a5650 100%)"></div>
  <div><h4>Grote meetdriehoek 12 inch | speed square winkelhaak meetgereedschap</h4><p>Bij het lassen komt veel uv licht vrij. Met verkeerde of te korte handschoenen zijn uw handen.</p></div>
</div>
<div class="abs feat" style="left:610px">
  <div class="ph" role="img" aria-label="Blue and yellow leather welding gloves" style="background:radial-gradient(ellipse 40% 30% at 40% 35%,#2c4fc4 0%,rgba(44,79,196,0) 100%),radial-gradient(ellipse 38% 32% at 55% 68%,#e3b02a 0%,rgba(227,176,42,0) 100%),#fff"></div>
  <div><h4>Welding gloves blue</h4><p>PREMIUM COWING LEATHER – Full cow split leather back to the cuff. Protection against rough objects, heat, sparks and flames. WEAR RESISTANT – With durable stitching to ensure your safety and durability of heat resistant.</p></div>
</div>

<!-- quote -->
<div class="abs quote-photo" role="img" aria-label="Welder in protective gear welding steel beams on a construction site"></div>
<svg class="abs" style="left:0;top:2952px" width="715" height="488" viewBox="0 0 715 488"><polygon points="0,0 715,0 632,488 0,488" fill="#17487d"/></svg>
<h2 class="abs quote-title">REQUEST A QUOTE</h2>
<div class="abs field" style="left:172px;top:3086px;width:200px;height:47px">Name</div>
<div class="abs field" style="left:390px;top:3086px;width:199px;height:47px">Email</div>
<div class="abs field" style="left:172px;top:3153px;width:417px;height:47px">Subject</div>
<div class="abs field" style="left:172px;top:3220px;width:417px;height:76px">Message</div>
<div class="abs submit">SUBMIT</div>

<!-- footer -->
<div class="abs foot-brand"><span class="brand-dot"></span>FusoBrite.com</div>
<div class="abs foot-col" style="left:450px;top:3568px"><h5>QUICK LINKS</h5><ul><li>Home</li><li>Products</li><li>Customer care</li><li>Informatie</li><li>Bronnen</li></ul></div>
<div class="abs foot-col about" style="left:592px;top:3568px"><h5>ABOUT US</h5><p>Een lasdruppel van ruim 1200 graden brand gemakkelijk door een goedkope bouwhand schoen heen. Ook bij oud vers leten handschoenen is een brandplek snel opgelopen.</p></div>
<div class="abs foot-col" style="left:825px;top:3568px"><h5>SUBSCRIBE US</h5></div>
<div class="abs email">Email Address</div>
<div class="abs sub-btn">SUBSCRIBE</div>
<div class="abs rule"></div>
<div class="abs copy">Copyrights @ 2021 FusoBrite. All Rights Reserved.</div>
<div class="abs social"><span></span><span></span><span></span><span></span><span></span></div>

</body>
</html>
```